Beauty website banner

We are an Australian beauty website selling mid and high end cosmetics and beauty products.

We need a banner that tells customers they can share their product wishlists with friends to let them know what they want for Christmas.

Target Market(s)

Female, 30-60, white collar

Industry/Entity Type

Cosmetics

Requirements
Must have
• 600 x 150 pixels in size

Words to be as follows, not including the (") of course.

"Share your wishlist with friends and family for Christmas!"

(Then in smaller font) "Just log in to your account, go to your wishlist and click on the ‘share wishlist’ button"

```html
<!DOCTYPE html>
<html lang="en">
<head>
<meta charset="utf-8">
<title>Share your wishlist for Christmas</title>
<link rel="stylesheet" href="https://fonts.googleapis.com/css2?family=Pinyon+Script&family=Playfair+Display:wght@400&family=Barlow+Semi+Condensed:wght@600&display=swap">
<style>
  :root {
    --page: #ffffff;
    --slate: #4a5e75;
    --band: #4c6078;
    --band-text: #ffffff;
    --wash-blue: #dbe6ef;
    --wash-lilac: #e9dcec;
    --wash-peach: #f3e6d6;
    --wash-mint: #e2eee5;
  }
  html, body {
    margin: 0;
    width: 1200px;
    height: 399px;
    overflow: hidden;
    background: var(--page);
  }
  .banner {
    display: block;
    width: 1200px;
    height: 399px;
  }
  .headline-script {
    font-family: "Pinyon Script", cursive;
    font-size: 50px;
    fill: var(--slate);
  }
  .headline-season {
    font-family: "Playfair Display", serif;
    font-size: 112px;
    fill: var(--slate);
  }
  .instruction {
    font-family: "Barlow Semi Condensed", sans-serif;
    font-weight: 600;
    font-size: 21px;
    fill: var(--band-text);
  }
</style>
</head>
<body>
<svg class="banner" viewBox="0 0 1200 399" xmlns="http://www.w3.org/2000/svg">
  <defs>
    <linearGradient id="floral-wash" x1="0" y1="0" x2="1" y2="1">
      <stop offset="0" stop-color="var(--wash-blue)"/>
      <stop offset="0.35" stop-color="var(--wash-lilac)"/>
      <stop offset="0.65" stop-color="var(--wash-peach)"/>
      <stop offset="1" stop-color="var(--wash-mint)"/>
    </linearGradient>
  </defs>

  <rect class="top-rule" x="101" y="74" width="994" height="7" fill="var(--slate)"/>

  <rect class="floral-backdrop" x="101" y="81" width="994" height="205" fill="url(#floral-wash)" opacity="0.7"
        role="img" aria-label="Soft pastel watercolour leaves and blossoms behind the headline"/>

  <text class="headline-script" x="598" y="134" text-anchor="middle"
        textLength="970" lengthAdjust="spacingAndGlyphs">Share your wishlist with friends and family for</text>

  <text class="headline-season" x="615" y="257" text-anchor="middle"
        textLength="790" lengthAdjust="spacing">CHRISTMAS</text>

  <rect class="instruction-band" x="101" y="286" width="994" height="37" fill="var(--band)"/>
  <text class="instruction" x="598" y="312" text-anchor="middle"
        textLength="970" lengthAdjust="spacingAndGlyphs">Just log in to your account, go to your wishlist and click on the ‘share wishlist’ button.</text>
</svg>
</body>
</html>
```